Anti Cellulite Treatment Massage Oil see link https://www.brindlemart.com/Anti-Cellulite-Treatment-Massa

i need a packaging design for Anti Cellulite Treatment Massage Oil like this
https://www.brindlemart.com/s/ref=nb_sb_noss?url=search-alias%3Daps&field-keywords=Anti+Cellulite+Treatment+Massage+Oil+

our company is talo see link below https://www.brindlemart.com/Tal%C3%B6-Beauty-Garcinia-Cambogia-Extract/dp/K73QX2M9R5/ref=sr_1_1_a_it?ie=UTF8&qid=1494884000&sr=8-1&keywords=talo

its a 8oz / 240 ml

Target Market(s)

health & beauty

Industry/Entity Type

Massage

Font styles to use
Serif
Sans Serif
Decorative
Script

Colors

Designer to choose colors to be used in the design.

Requirements
Must have
• our logo and pump like this seller
• https://www.brindlemart.com/Anti-Cellulite-Treatment-Massage-Oil/dp/K94RT6P2W8/ref=sr_1_1_a_it?ie=UTF8&qid=1494884194&sr=8-1&keywords=+Anti+Cellulite+Treatment+Massage+Oil
Nice to have
• the most similar to this or even better idea from this link
Should not have
• pictures on the label

```html
<!DOCTYPE html>
<html lang="en">
<head>
<meta charset="utf-8">
<title>talo Anti Cellulite Massage Oil – Label</title>
<link href="https://fonts.googleapis.com/css2?family=Playfair+Display:wght@700&family=Montserrat:wght@400;500&family=Pinyon+Script&family=Open+Sans:ital,wght@1,400;1,600&display=swap" rel="stylesheet">
<style>
  :root {
    --backdrop: #ececec;
    --label-pink: #e5c2dc;
    --label-pink-light: #efd3e7;
    --gold: #b39457;
    --gold-dark: #7d6230;
    --ink-grey: #5d5862;
    --soft-white: #fbf3f8;
  }
  * { margin: 0; padding: 0; box-sizing: border-box; }
  html, body {
    width: 1200px;
    height: 867px;
    overflow: hidden;
    background: var(--backdrop);
  }
  .canvas {
    position: relative;
    width: 1200px;
    height: 867px;
  }
  .label {
    position: absolute;
    left: 220px;
    top: 108px;
    width: 760px;
    height: 650px;
    background: radial-gradient(ellipse at 50% 40%, var(--label-pink-light) 0%, var(--label-pink) 70%);
    overflow: hidden;
    box-shadow: 0 2px 10px rgba(0,0,0,0.06);
  }
  .label__band {
    position: absolute;
    left: 0;
    width: 100%;
    height: 16px;
    background: linear-gradient(to bottom, var(--gold-dark), var(--gold) 45%, var(--gold-dark));
  }
  .label__band--top { top: 0; }
  .label__band--bottom { bottom: 0; }
  .label__band::after {
    content: "";
    position: absolute;
    left: 0;
    width: 100%;
    height: 2px;
    background: var(--gold);
  }
  .label__band--top::after { bottom: -8px; }
  .label__band--bottom::after { top: -8px; }

  .label__silhouette {
    position: absolute;
    left: 250px;
    top: 150px;
    width: 260px;
    height: 440px;
    border-radius: 45% 45% 40% 40%;
    background: radial-gradient(ellipse at center, rgba(255,255,255,0.18), rgba(255,255,255,0) 70%);
  }

  .brand {
    position: absolute;
    top: 64px;
    left: 0;
    width: 100%;
    display: flex;
    justify-content: center;
    align-items: center;
    gap: 22px;
  }
  .brand__mark {
    width: 56px;
    height: 56px;
    border-radius: 50%;
    border: 4px solid #ffffff;
  }
  .brand__name {
    font-family: "Montserrat", sans-serif;
    font-weight: 400;
    font-size: 62px;
    color: #ffffff;
    letter-spacing: 1px;
    line-height: 1;
  }

  .product-title {
    position: absolute;
    top: 222px;
    width: 100%;
    text-align: center;
    font-family: "Playfair Display", serif;
    font-weight: 700;
    font-size: 60px;
    letter-spacing: 3px;
    color: var(--gold);
    text-transform: uppercase;
  }
  .product-type {
    position: absolute;
    top: 312px;
    width: 100%;
    text-align: center;
    font-family: "Montserrat", sans-serif;
    font-weight: 500;
    font-size: 48px;
    letter-spacing: 2px;
    color: var(--ink-grey);
  }
  .tagline {
    position: absolute;
    top: 402px;
    width: 100%;
    text-align: center;
    font-family: "Pinyon Script", cursive;
    font-size: 36px;
    color: var(--ink-grey);
  }
  .description {
    position: absolute;
    top: 468px;
    left: 110px;
    width: 540px;
    text-align: center;
    font-family: "Open Sans", sans-serif;
    font-style: italic;
    font-size: 20px;
    line-height: 1.3;
    color: var(--soft-white);
  }
  .description strong { font-weight: 600; }
  .volume {
    position: absolute;
    top: 586px;
    width: 100%;
    text-align: center;
    font-family: "Montserrat", sans-serif;
    font-weight: 500;
    font-size: 24px;
    color: var(--ink-grey);
  }
</style>
</head>
<body>
<div class="canvas">
  <section class="label">
    <div class="label__band label__band--top"></div>
    <div class="label__silhouette" role="img" aria-label="Faint line drawing of a body silhouette"></div>

    <div class="brand">
      <span class="brand__mark"></span>
      <span class="brand__name">talo</span>
    </div>

    <h1 class="product-title">Anti Cellulite</h1>
    <p class="product-type">• MASSAGE OIL •</p>
    <p class="tagline">All Natural Ingredients</p>
    <p class="description"><strong>BEST CELLULITE TREATMENT</strong> this aromatic oil helps eliminate toxins and deliver and overall feeling of wellbeing</p>
    <p class="volume">8 fl Oz / 240 ml</p>

    <div class="label__band label__band--bottom"></div>
  </section>
</div>
</body>
</html>
```